Web Design for ORV Air conditioning company

Hello,

I am calling on you for the modernization of the company's website
https://clim-solaris-atelier.fr/

The new one must include the new logo with the new graphic charter (color, style ...)

I'm looking for a simple design (less is more), a font written without Serif, the logo that brings a touch of color and modernity.

(maintenance and installation company for air conditioning and ventilation systems)
COLORS: in line with the logo

CHAPTER:

# PRESENTATION
# SERVICES
AIR CONDITIONING (ice cube icon)
HEATING (flame icon)
AIR TREATMENT (icon fan)
# ACHIEVEMENTS

# CONTACT
CONTACT FORM
GOOGLE MAPS

Target Market(s)

Showcase site for our customers

Coding

Coded - Design and coding required

Number of Pages Required

4 page

Font styles to use
Sans Serif

Colors
33b8a4
33a6d7
3176b5
ffffff

Requirements
Must have
• Clear and fluid navigation
a visual identity of the page with the logo
Should not have
• Overloaded.

```html
<!DOCTYPE html>
<html lang="en">
<head>
<meta charset="utf-8">
<title>ORV – Air Conditioning, Heating & Air Treatment</title>
<link rel="stylesheet" href="https://fonts.googleapis.com/css2?family=Poppins:wght@400;500;600;700;800&display=swap">
<style>
:root{
  --teal:#33b8a4;
  --blue:#33a6d7;
  --deep:#3176b5;
  --ink:#2d3e4e;
  --ink-2:#3a4a58;
  --grey:#6b7680;
  --line:#d9dee2;
  --white:#ffffff;
  --field:#e6e8ea;
}
*{box-sizing:border-box;margin:0;padding:0}
html,body{width:1200px;height:4000px;overflow:hidden}
body{font-family:'Poppins',sans-serif;color:var(--ink);background:var(--white);position:relative}
.abs{position:absolute}

/* header */
.site-header{top:0;left:0;width:1200px;height:97px;background:var(--white);border-top:4px solid var(--blue);z-index:5}
.brand{left:66px;top:16px;font-size:54px;font-weight:800;color:var(--teal);letter-spacing:2px;line-height:60px}
.main-nav{left:407px;top:36px;display:flex;gap:28px;font-size:14px;font-weight:500;color:var(--ink)}
.main-nav a{color:inherit;text-decoration:none;padding-bottom:8px}
.main-nav a.active{color:var(--blue);border-bottom:3px solid var(--blue)}
.hotline{left:918px;top:20px;display:flex;align-items:center;gap:12px}
.hotline .ring{width:52px;height:52px;border:3px solid var(--blue);border-radius:50%;display:flex;align-items:center;justify-content:center}
.hotline small{display:block;color:var(--teal);font-size:14px;font-weight:600}
.hotline strong{display:block;font-size:22px;font-weight:700;color:var(--ink);line-height:26px}

/* hero */
.hero-photo{top:97px;left:0;width:1200px;height:680px;background:linear-gradient(100deg,#eceeee 0%,#d8dcdd 40%,#9fb3c6 62%,#dfe3e4 85%,#c9cfd2 100%)}
.hero-curve{top:690px;left:0;width:1200px;height:110px}
.hero-copy{left:145px;top:290px}
.hero-copy h1{font-size:44px;font-weight:800;line-height:54px;color:#1f2a33}
.hero-copy p{margin-top:14px;font-size:20px;font-weight:500;color:#1f2a33}
.btn{display:inline-block;font-size:15px;font-weight:600;padding:0 34px;height:46px;line-height:46px;text-decoration:none}
.btn-fill{background:linear-gradient(90deg,var(--teal),var(--blue));color:var(--white)}
.btn-light{background:var(--white);color:var(--ink);margin-left:12px;padding:0 28px}
.hero-copy .actions{margin-top:26px}
.slider-arrow{width:50px;height:50px;border-radius:50%;display:flex;align-items:center;justify-content:center}
.arrow-prev{left:42px;top:380px;border:2px solid rgba(255,255,255,.7)}
.arrow-next{left:1107px;top:380px;background:var(--blue)}

/* services */
.services-bg{top:800px;left:0;width:1200px;height:560px;background:radial-gradient(circle at 10% 30%,#eef4f8 0,transparent 30%),radial-gradient(circle at 92% 70%,#eef4f8 0,transparent 25%)}
.section-title{font-size:44px;font-weight:700;color:var(--ink);text-align:center;width:1200px;left:0}
.section-title span{color:var(--teal)}
.title-services{top:855px}
.service{width:300px;height:300px;border-radius:50%;border:4px solid var(--ink);background:var(--ink-2);color:var(--white);text-align:center}
.service.featured{background:var(--blue);border-color:#2b8fc0}
.service .badge{position:absolute;left:75px;top:-74px;width:150px;height:150px;border-radius:50%;background:var(--white);display:flex;align-items:center;justify-content:center}
.service h3{position:absolute;top:124px;width:100%;font-size:21px;font-weight:600}
.service p{position:absolute;top:160px;left:48px;width:204px;font-size:12px;line-height:19px;opacity:.9}
.service .more{position:absolute;left:132px;top:232px}

/* about */
.about-band{top:1380px;left:0;width:1200px;height:625px}
.about-copy{left:124px;top:1560px;width:430px;color:var(--white)}
.about-copy h2{font-size:44px;font-weight:700;line-height:56px}
.about-copy h4{font-size:28px;font-weight:700;line-height:40px}
.about-copy p{margin-top:16px;font-size:17px;line-height:26px}
.btn-ghost{margin-top:28px;border:2px solid var(--white);border-radius:26px;color:var(--white);height:48px;line-height:44px;padding:0 28px}
.about-mark{left:598px;top:1560px;width:510px;text-align:center;font-size:270px;font-weight:800;line-height:300px;color:var(--white);letter-spacing:8px}

/* process */
.title-process{top:2095px;font-size:38px}
.process-photo{left:395px;top:2218px;width:374px;height:374px;border-radius:50%;background:radial-gradient(circle at 40% 45%,#4b6c96 0,#283b5c 45%,#c5cbd2 75%,#e7eaec 100%);border:5px solid var(--white);box-shadow:0 0 0 4px var(--blue)}
.step-icon{width:96px;height:96px;border-radius:50%;background:var(--white);border:3px solid var(--blue);display:flex;align-items:center;justify-content:center}
.step h3{font-size:20px;font-weight:700;color:var(--ink)}
.step p{font-size:13px;line-height:21px;color:var(--grey);margin-top:6px}
.step-install{left:170px;top:2202px;width:205px;text-align:right}
.step-trouble{left:843px;top:2346px;width:220px}
.step-maint{left:205px;top:2540px;width:205px;text-align:right}

/* testimonials */
.testi-blue{top:2740px;left:0;width:1200px;height:442px}
.testi-photo{top:2740px;left:550px;width:650px;height:442px}
.testi-card{left:132px;top:2828px;width:573px;height:266px;background:var(--white);padding:38px 42px}
.testi-card h2{font-size:32px;font-weight:700}
.testi-card h2 span{color:var(--teal)}
.testi-card p{margin-top:14px;font-size:14px;line-height:24px;color:var(--ink)}
.testi-card .who{margin-top:10px;font-size:18px;font-weight:600;color:var(--deep)}
.testi-nav{left:88px;width:44px;height:48px;background:var(--white);display:flex;align-items:center;justify-content:center}

/* contact */
.map{top:3182px;left:0;width:640px;height:442px}
.contact{left:668px;top:3250px;width:445px}
.contact h2{font-size:34px;font-weight:700;color:var(--ink)}
.form{margin-top:22px;display:grid;grid-template-columns:1fr 1fr;gap:12px 10px}
.field{height:37px;background:var(--field);border:1px solid var(--line);font-size:13px;color:var(--grey);padding:9px 12px}
.field.wide{grid-column:1/3;height:98px}
.submit{margin-top:14px;background:var(--deep);color:var(--white);font-size:15px;font-weight:600;width:120px;height:42px;line-height:42px;text-align:center}

/* footer */
.footer{top:3624px;left:0;width:1200px;height:376px;background:var(--ink);color:var(--white)}
.foot-brand{left:128px;top:3680px;font-size:96px;font-weight:800;letter-spacing:4px;line-height:110px}
.socials{left:168px;top:3808px;display:flex;gap:8px}
.socials span{width:32px;height:32px;border-radius:50%;border:1.5px solid #6c7a86;display:block}
.foot-col h4{font-size:20px;font-weight:600;margin-bottom:8px}
.foot-col li{list-style:none;font-size:14px;line-height:27px;color:#c6ccd2}
.col-contact{left:422px;top:3694px}
.col-contact li{display:flex;gap:10px;align-items:flex-start;margin-bottom:6px;line-height:20px}
.col-company{left:740px;top:3694px}
.col-services{left:948px;top:3694px}
.copyright{top:3914px;left:0;width:1200px;border-top:1px solid #45555f;padding-top:24px;text-align:center;font-size:14px;color:#c6ccd2}
</style>
</head>
<body>

<header class="site-header abs">
  <div class="brand abs">ORV</div>
  <nav class="main-nav abs">
    <a class="active" href="#">HOME</a><a href="#">ABOUT</a><a href="#">SERVICES ▾</a><a href="#">ACHIEVEMENTS</a><a href="#">CONTACT</a>
  </nav>
  <div class="hotline abs">
    <div class="ring"><svg width="24" height="24" viewBox="0 0 24 24"><path d="M6.6 10.8a15 15 0 0 0 6.6 6.6l2.2-2.2a1 1 0 0 1 1-.25 11 11 0 0 0 3.6.6 1 1 0 0 1 1 1V20a1 1 0 0 1-1 1A17 17 0 0 1 3 4a1 1 0 0 1 1-1h3.5a1 1 0 0 1 1 1c0 1.25.2 2.45.6 3.6a1 1 0 0 1-.25 1z" fill="var(--blue)"/></svg></div>
    <div><small>24/7 fast service</small><strong>1 800 555 0142</strong></div>
  </div>
</header>

<div class="hero-photo abs" role="img" aria-label="Technician in blue overalls servicing a wall-mounted air conditioner while a smiling customer watches, white brick wall"></div>
<svg class="hero-curve abs" viewBox="0 0 1200 110" preserveAspectRatio="none">
  <path d="M0 0 L0 110 L1200 110 L1200 0 Q900 20 600 80 Q300 20 0 0Z" fill="var(--white)"/>
  <path d="M0 8 Q300 28 600 88 Q900 28 1200 8 L1200 0 Q900 16 600 74 Q300 16 0 0Z" fill="var(--blue)"/>
</svg>
<div class="hero-copy abs">
  <h1>CLIM SOLARIS<br>ATELIER<br>LYON</h1>
  <p>THE SOLUTION TO YOUR MAINTENANCE PROBLEM</p>
  <div class="actions"><a class="btn btn-fill" href="#">READ MORE</a><a class="btn btn-light" href="#">GET A QUOTE</a></div>
</div>
<div class="slider-arrow arrow-prev abs"><svg width="18" height="18" viewBox="0 0 18 18"><path d="M11 3 5 9l6 6" stroke="#fff" stroke-width="2" fill="none"/></svg></div>
<div class="slider-arrow arrow-next abs"><svg width="18" height="18" viewBox="0 0 18 18"><path d="M7 3l6 6-6 6" stroke="#fff" stroke-width="2.5" fill="none"/></svg></div>

<div class="services-bg abs"></div>
<h2 class="section-title title-services abs">OUR <span>SERVICES</span></h2>

<div class="service abs" style="left:129px;top:975px">
  <div class="badge"><svg width="78" height="78" viewBox="0 0 78 78" fill="none" stroke="var(--ink)" stroke-width="2.5"><path d="M8 20l22-8 16 10-22 8z"/><path d="M8 20v24l16 10V30"/><path d="M24 54l22-8V22"/><path d="M36 40l22-6 14 10-22 6z"/><path d="M36 40v22l14 10V50"/><path d="M50 72l22-6V44"/></svg></div>
  <h3>AIR CONDITIONING</h3>
  <p>Lorem ipsum dolor sit amet, consectetur adipisicing elit, sed do eiusmod tempor</p>
  <svg class="more" width="36" height="36" viewBox="0 0 36 36" fill="none" stroke="#fff" stroke-width="2"><circle cx="18" cy="18" r="16"/><path d="M11 15l7 7 7-7"/></svg>
</div>
<div class="service featured abs" style="left:450px;top:975px">
  <div class="badge"><svg width="72" height="78" viewBox="0 0 72 78" fill="none" stroke="var(--blue)" stroke-width="3"><path d="M30 74C12 70 6 52 16 38c2 8 6 10 8 10C20 30 30 14 40 4c0 14 14 22 14 38 4-2 6-6 6-10 10 16 2 38-18 42"/><path d="M34 74c-8-4-8-14 0-22 0 6 4 8 6 8 0-6 2-10 6-12 2 12 0 22-12 26"/></svg></div>
  <h3>HEATING</h3>
  <p>Lorem ipsum dolor sit amet, consectetur adipisicing elit, sed do eiusmod tempor</p>
  <svg class="more" width="36" height="36" viewBox="0 0 36 36" fill="none" stroke="#fff" stroke-width="2"><circle cx="18" cy="18" r="16"/><path d="M11 15l7 7 7-7"/></svg>
</div>
<div class="service abs" style="left:769px;top:975px">
  <div class="badge"><svg width="80" height="80" viewBox="0 0 80 80" fill="none" stroke="var(--ink)" stroke-width="3"><circle cx="40" cy="40" r="36"/><circle cx="40" cy="40" r="7"/><path d="M40 33C36 22 38 12 44 8M47 40c11-2 20 2 24 8M43 47c6 10 6 19 2 24M33 40c-11 3-20 0-25-5M37 33c-7-8-10-16-8-22"/></svg></div>
  <h3>AIR TREATMENT</h3>
  <p>Lorem ipsum dolor sit amet, consectetur adipisicing elit, sed do eiusmod tempor</p>
  <svg class="more" width="36" height="36" viewBox="0 0 36 36" fill="none" stroke="#fff" stroke-width="2"><circle cx="18" cy="18" r="16"/><path d="M11 15l7 7 7-7"/></svg>
</div>

<svg class="about-band abs" viewBox="0 0 1200 625" preserveAspectRatio="none" role="img" aria-label="Teal to blue band over a photo of a technician checking pressure gauges">
  <defs><linearGradient id="aboutGrad" x1="0" y1="0" x2="1" y2="0"><stop offset="0" stop-color="var(--teal)"/><stop offset="0.55" stop-color="#2f8fc4"/><stop offset="1" stop-color="var(--deep)"/></linearGradient></defs>
  <path d="M0 70 L600 0 L1200 60 L1200 625 L0 625Z" fill="var(--ink)"/>
  <path d="M0 82 L600 14 L1200 72 L1200 625 L0 625Z" fill="url(#aboutGrad)"/>
</svg>
<div class="about-copy abs">
  <h2>About ventaro</h2>
  <h4>Data Management</h4>
  <p>Lorem Ipsum is simply dummy text of the printing and typesetting industry. Lorem Ipsum has been industry's standard dummy text ever since the</p>
  <p>1500s, when an unknown printer took a galley of type and scrambled Lorem Ipsum is simply.</p>
  <a class="btn btn-ghost" href="#">LEARN MORE</a>
</div>
<div class="about-mark abs">ORV</div>

<h2 class="section-title title-process abs">REVERSIBLE &nbsp;<span>CLIMATE CONTROL</span></h2>
<svg class="abs" style="left:330px;top:2170px" width="480" height="480" viewBox="0 0 480 480" fill="none" stroke="#aab4bd" stroke-width="2" stroke-dasharray="8 7">
  <path d="M298 18c40 4 70 24 86 54"/><path d="M38 140c-10 30-8 60 8 88"/><path d="M436 358c-8 34-36 56-72 66"/>
</svg>
<div class="process-photo abs" role="img" aria-label="Hands holding refrigerant pressure gauges beside an outdoor condenser unit"></div>
<div class="step-icon abs" style="left:408px;top:2207px"><svg width="50" height="50" viewBox="0 0 50 50" fill="none" stroke="var(--ink)" stroke-width="2.5"><path d="M10 40l20-20M8 8l8 2 2 8M34 6a8 8 0 0 0 8 12L24 36a4 4 0 1 1-6-6L36 12"/></svg></div>
<div class="step-icon abs" style="left:723px;top:2347px"><svg width="50" height="50" viewBox="0 0 50 50" fill="none" stroke="var(--ink)" stroke-width="2.5"><rect x="6" y="10" width="38" height="26" rx="2"/><path d="M18 44h14M25 36v8M14 24l6-6 6 6 8-8"/></svg></div>
<div class="step-icon abs" style="left:446px;top:2525px"><svg width="50" height="50" viewBox="0 0 50 50" fill="none" stroke="var(--ink)" stroke-width="2.5"><circle cx="25" cy="25" r="7"/><path d="M25 5v7M25 38v7M5 25h7M38 25h7M11 11l5 5M34 34l5 5M11 39l5-5M34 16l5-5"/><circle cx="25" cy="25" r="14"/></svg></div>
<div class="step step-install abs"><h3>INSTALLATION</h3><p>Lorem Ipsum is simply dummy text of the printing typesetting Lorem Ipsum has been</p></div>
<div class="step step-trouble abs"><h3>TROUBLESHOOTING</h3><p>Lorem Ipsum is simply dummy text of the printing typesetting Lorem Ipsum has been</p></div>
<div class="step step-maint abs"><h3>MAINTENANCE</h3><p>Lorem Ipsum is simply dummy text of the printing typesetting Lorem Ipsum has been</p></div>

<div class="testi-photo abs" role="img" aria-label="Smiling couple sitting together on a sofa in a bright living room" style="background:linear-gradient(120deg,#cfc7bd 0%,#a89a8a 45%,#5a6e86 75%,#c9c2b8 100%)"></div>
<svg class="testi-blue abs" viewBox="0 0 1200 442" preserveAspectRatio="none"><path d="M0 0H552L642 442H0Z" fill="var(--blue)"/></svg>
<div class="testi-nav abs" style="top:2910px"><svg width="16" height="20" viewBox="0 0 16 20"><path d="M11 3 4 10l7 7" stroke="var(--ink)" stroke-width="3" fill="none"/></svg></div>
<div class="testi-nav abs" style="top:2962px"><svg width="16" height="20" viewBox="0 0 16 20"><path d="M5 3l7 7-7 7" stroke="var(--ink)" stroke-width="3" fill="none"/></svg></div>
<div class="testi-card abs">
  <h2>CUSTOMER <span>TESTIMONIALS</span></h2>
  <p>Lorem Ipsum is simply dummy text of the printing and typesetting industry. Lorem Ipsum has been the industry's standard dummy text ever since the 1500s Lorem Ipsum is simply dummy text of the printing and typesetting industry. Lorem Ipsum <b style="font-size:26px;color:var(--ink)">”</b></p>
  <div class="who">Customer Name</div>
</div>

<svg class="map abs" viewBox="0 0 640 442" preserveAspectRatio="none" role="img" aria-label="Street map showing the company location">
  <path d="M0 0H640L560 442H0Z" fill="#eceae6"/>
</svg>
<div class="contact abs">
  <h2>CONTACT</h2>
  <div class="form">
    <div class="field">Name</div><div class="field">Phone No</div>
    <div class="field">Email Address</div><div class="field">Subject</div>
    <div class="field wide">Message</div>
  </div>
  <div class="submit">SUBMIT</div>
</div>

<footer class="footer abs"></footer>
<div class="foot-brand abs" style="color:var(--white)">ORV</div>
<div class="socials abs" aria-label="Social media links"><span></span><span></span><span></span><span></span></div>
<div class="foot-col col-contact abs">
  <h4>CONTACT US</h4>
  <ul>
    <li><svg width="14" height="18" viewBox="0 0 14 18"><path d="M7 1a6 6 0 0 0-6 6c0 5 6 10 6 10s6-5 6-10a6 6 0 0 0-6-6zm0 8a2 2 0 1 1 0-4 2 2 0 0 1 0 4z" fill="#c6ccd2"/></svg><span>14 Rue des Tilleuls<br>69003 LYON</span></li>
    <li><svg width="16" height="16" viewBox="0 0 24 24"><path d="M6.6 10.8a15 15 0 0 0 6.6 6.6l2.2-2.2a1 1 0 0 1 1-.25 11 11 0 0 0 3.6.6 1 1 0 0 1 1 1V20a1 1 0 0 1-1 1A17 17 0 0 1 3 4a1 1 0 0 1 1-1h3.5a1 1 0 0 1 1 1c0 1.25.2 2.45.6 3.6a1 1 0 0 1-.25 1z" fill="#c6ccd2"/></svg><span>04 72 10 20 30</span></li>
    <li style="margin-top:14px"><svg width="16" height="12" viewBox="0 0 16 12"><rect x="0.5" y="0.5" width="15" height="11" fill="none" stroke="#c6ccd2"/><path d="M1 1l7 6 7-6" stroke="#c6ccd2" fill="none"/></svg><span>info@companyname.com</span></li>
  </ul>
</div>
<div class="foot-col col-company abs">
  <h4>COMPANY</h4>
  <ul><li>Home</li><li>About Us</li><li>Achievements</li><li>Contact Us</li></ul>
</div>
<div class="foot-col col-services abs">
  <h4>SERVICES</h4>
  <ul><li>Air Conditioning</li><li>Heating</li><li>Air Treatment</li><li>Testimonials</li></ul>
</div>
<div class="copyright abs">© 2020 Clim Solaris Atelier. All Rights are Reserved.</div>

</body>
</html>
```